Real Estate Company / Capital Needs Cards!

need business cards designed using the logos that were just designed by sketchhive.

Reason: per designers request deadline extended 1 day…thank you.

Target Market(s)

Investors and clients looking to purchase real estate or invest in the business.

Industry/Entity Type

Business

Requirements
Must have
• two designs - one for the real estate logo and one for the capital logo, similar but slightly different.
Nice to have
• something to make it pop (perhaps on the back)
Should not have
• much color

```html
<!DOCTYPE html>
<html lang="en">
<head>
<meta charset="utf-8">
<title>Verano Real Estate – Business Cards</title>
<link rel="stylesheet" href="https://fonts.googleapis.com/css2?family=Source+Sans+3:wght@400;600&display=swap">
<style>
  :root {
    --backdrop: #e9e7e4;
    --card: #ffffff;
    --panel: #6d6e71;
    --stripe: #a7a9ac;
    --ink-light: #ffffff;
    --ink-brand: #6d6e71;
    --ink-dark: #3a3a3c;
  }
  * { box-sizing: border-box; margin: 0; padding: 0; }
  html, body { width: 1200px; height: 498px; overflow: hidden; background: var(--backdrop); }
  body { position: relative; font-family: "Source Sans 3", "Helvetica Neue", Arial, sans-serif; }

  .card {
    position: absolute;
    top: 99px;
    width: 540px;
    height: 300px;
    background: var(--card);
    box-shadow: 0 6px 18px rgba(0,0,0,0.18);
    overflow: hidden;
  }
  .card--front { left: 40px; }
  .card--back  { left: 620px; }

  .front-shape { position: absolute; inset: 0; }

  .brand {
    position: absolute;
    display: flex;
    align-items: center;
    color: var(--ink-brand);
    font-weight: 400;
  }
  .brand__square { background: var(--ink-brand); flex: none; }
  .brand__name { line-height: 1.05; letter-spacing: 0.06em; text-transform: uppercase; }

  .card--front .brand { left: 46px; top: 124px; gap: 10px; }
  .card--front .brand__square { width: 40px; height: 40px; }
  .card--front .brand__name { font-size: 21px; }

  .contact {
    position: absolute;
    right: 26px;
    top: 40px;
    text-align: right;
    color: var(--ink-light);
  }
  .contact__name { font-size: 21px; font-weight: 600; line-height: 1.1; }
  .contact__title { font-size: 15px; margin-bottom: 30px; }
  .contact__line { font-size: 16px; line-height: 1.25; display: flex; justify-content: flex-end; align-items: center; gap: 4px; }
  .contact__phones { margin-bottom: 28px; }
  .contact__address { font-size: 15px; line-height: 1.3; margin-bottom: 24px; }
  .contact__line svg { width: 12px; height: 12px; fill: var(--ink-light); }

  .card--back .brand { left: 95px; top: 110px; gap: 18px; }
  .card--back .brand__square { width: 66px; height: 66px; }
  .card--back .brand__name { font-size: 38px; }

  .website {
    position: absolute;
    left: 0; right: 0;
    top: 212px;
    text-align: center;
    font-size: 16px;
    letter-spacing: 0.14em;
    color: var(--ink-dark);
  }
  .website strong { font-weight: 600; }
</style>
</head>
<body>

<section class="card card--front" aria-label="Business card front">
  <svg class="front-shape" viewBox="0 0 540 300" preserveAspectRatio="none" aria-hidden="true">
    <path d="M294 0 Q338 150 228 300 L540 300 L540 0 Z" fill="var(--stripe)"/>
    <path d="M312 0 Q356 150 244 300 L540 300 L540 0 Z" fill="var(--card)"/>
    <path d="M318 0 Q362 150 250 300 L540 300 L540 0 Z" fill="var(--panel)"/>
  </svg>

  <div class="brand">
    <span class="brand__square"></span>
    <span class="brand__name">Verano<br>Real Estate</span>
  </div>

  <div class="contact">
    <p class="contact__name">Your Name</p>
    <p class="contact__title">Title</p>
    <div class="contact__phones">
      <p class="contact__line">
        <svg viewBox="0 0 12 12"><path d="M2.5 1 L4.5 1 L5 3.5 L3.8 4.4 Q4.8 6.6 7.6 8.2 L8.5 7 L11 7.5 L11 9.5 Q10 11 8.5 11 Q2 9 1 3.5 Q1 2 2.5 1 Z"/></svg>
        123-456-7980
      </p>
      <p class="contact__line">
        <svg viewBox="0 0 12 12"><rect x="3" y="1" width="6" height="4"/><rect x="1" y="5" width="10" height="5" rx="1"/><rect x="3" y="9" width="6" height="2.5"/></svg>
        123-568-7896
      </p>
    </div>
    <p class="contact__address">Street Name City Name<br>State ZipCode</p>
    <p class="contact__line">
      <svg viewBox="0 0 12 12"><path d="M1 4 L6 1 L11 4 L11 11 L1 11 Z"/><path d="M1 4 L6 7.5 L11 4" fill="none" stroke="var(--panel)" stroke-width="1"/></svg>
      veranorealestate@mailbox.com
    </p>
  </div>
</section>

<section class="card card--back" aria-label="Business card back">
  <div class="brand">
    <span class="brand__square"></span>
    <span class="brand__name">Verano<br>Real Estate</span>
  </div>
  <p class="website">www.<strong>veranorealestate</strong>.com</p>
</section>

</body>
</html>
```